VORLANE (PTY)LTD Website design

WEBSITE design based on our different divisions in our organization.
Our company specializes in the following.
Construction
Property development
Demolition
Mining
Transport
Manufacturing of concrete bricks and blocks
Lightweight concrete Readymix
I want a very modern website and look that fits in with our organization and the changing times of the world.
The website must be very professional and crisp and should appeal to both the younger generation and older generation of business leaders and.
The website must be very user friendly and easy to navigate, simple yet modern, professional and corporate.

```html
<!DOCTYPE html>
<html lang="en">
<head>
<meta charset="utf-8">
<title>VORLANE (PTY)LTD</title>
<link href="https://fonts.googleapis.com/css2?family=Raleway:wght@300;400;500;600;700&family=Lato:wght@400;700&display=swap" rel="stylesheet">
<style>
:root{
  --blue:#1e88d2;
  --blue-dark:#1a6fb3;
  --ink:#333;
  --muted:#666;
  --light:#f3f3f3;
  --line:#e3e3e3;
  --footer:#1b1b1b;
  --footer-base:#121212;
  --white:#fff;
}
*{margin:0;padding:0;box-sizing:border-box}
html,body{width:1200px;height:3309px;overflow:hidden}
body{position:relative;font-family:"Lato",sans-serif;color:var(--ink);background:var(--white)}
.abs{position:absolute}

/* top bar */
.topbar{left:0;top:0;width:1200px;height:41px;background:var(--light);border-bottom:1px solid var(--line)}
.topbar .cell{position:absolute;top:0;height:41px;border-left:1px solid #ddd;border-right:1px solid #ddd;display:flex;align-items:center;font-size:13px;color:#888;gap:8px}
.social{left:89px;width:230px;justify-content:center;gap:13px}
.social span{width:10px;height:10px;border-radius:50%;background:#999;display:block}
.contact-mail{left:690px;width:227px;justify-content:center}
.contact-phone{left:917px;width:194px;justify-content:center;border-left:none}

/* wordmark */
.brand{left:0;top:41px;width:1200px;height:86px;display:flex;align-items:center;justify-content:center}
.brand-name{font-family:"Raleway",sans-serif;font-weight:700;font-size:44px;color:var(--blue-dark);line-height:1;letter-spacing:1px}

/* nav */
.nav{left:0;top:127px;width:1200px;height:64px;background:var(--light);display:flex;justify-content:center;align-items:center;gap:27px;font-family:"Raleway",sans-serif;font-size:16.5px;color:#555}
.nav .active{color:var(--blue);border:2px solid var(--blue);padding:0 6px;line-height:18px}

/* hero */
.hero{left:0;top:191px;width:1200px;height:580px;background:linear-gradient(100deg,#6b5a48 0%,#a88d6c 25%,#5d4b3a 55%,#2e2620 100%)}
.hero-shade{left:0;top:191px;width:1200px;height:580px;background:linear-gradient(90deg,rgba(0,0,0,0) 30%,rgba(0,0,0,.35) 100%)}
.hero-title{right:95px;top:378px;font-family:"Raleway",sans-serif;font-weight:300;font-size:58px;color:var(--white);line-height:1}
.hero-title b{font-weight:700}
.hero-sub{right:95px;top:455px;width:440px;text-align:right;font-size:19px;line-height:31px;color:var(--white)}
.btn{display:flex;align-items:center;justify-content:center;font-family:"Raleway",sans-serif;font-weight:500;color:var(--white);background:var(--blue);font-size:16px;gap:6px}
.btn-hero{top:531px;height:36px}
.btn-outline{background:transparent;border:2px solid var(--white)}

/* section headings */
.sec-title{font-family:"Raleway",sans-serif;font-size:37px;line-height:1;display:flex;align-items:center;padding-left:16px;border-left:4px solid var(--blue);border-top:4px solid var(--blue);border-bottom:4px solid var(--blue);color:var(--blue)}
.sec-title b{font-weight:600}
.sec-title span{font-weight:300;margin-left:8px}
.sec-title.light{border-color:var(--white);color:var(--white)}

/* about */
.about-frame{left:501px;top:947px;width:608px;height:370px;border:2px solid var(--blue)}
.about-photo{left:89px;top:966px;width:512px;height:332px;background:linear-gradient(135deg,#c9a98a,#8d6f55 45%,#d8c2a5 80%,#b07a3a);border:2px solid #c6dced}
.about-h{left:624px;top:1000px;font-family:"Raleway",sans-serif;font-weight:500;font-size:28px;color:#222}
.about-p{left:624px;top:1040px;width:458px;font-size:15.5px;line-height:29px;color:var(--muted);text-align:justify}

/* services */
.services{left:0;top:1392px;width:1200px;height:535px;background:linear-gradient(110deg,#3a3a3a,#4c4a44 40%,#37382f 70%,#5a5b2e 100%)}
.services-shade{left:0;top:1392px;width:1200px;height:535px;background:rgba(20,20,20,.45)}
.svc{top:1568px;width:325px;height:285px;border:1px solid rgba(255,255,255,.85);color:var(--white);text-align:center;padding-top:36px}
.svc svg{display:block;margin:0 auto}
.svc h3{font-family:"Raleway",sans-serif;font-weight:600;font-size:18px;margin-top:24px;letter-spacing:.3px}
.svc p{font-size:16.5px;line-height:22.5px;margin:12px auto 0;width:270px}
.arrow{top:1692px;width:34px;height:34px}

/* testimonials */
.quote{top:2104px;width:487px;height:159px;border:1px solid var(--line);padding:14px 34px 0 18px;font-size:16.5px;line-height:26.5px;color:var(--muted)}
.avatar{width:72px;height:72px;border-radius:50%;background:radial-gradient(circle at 50% 40%,#c8a48a,#6e5444)}
.person{font-size:16.5px;color:var(--muted);font-weight:700}

/* news */
.news-bg{left:0;top:2377px;width:1200px;height:585px;background:linear-gradient(180deg,#ececec,#e4e4e4)}
.news{top:2548px;width:315px}
.news .pic{height:154px}
.news h4{font-family:"Raleway",sans-serif;font-weight:600;font-size:16px;color:var(--blue);margin-top:23px}
.news .meta{font-size:13px;color:#aaa;margin-top:10px;padding-bottom:6px;border-bottom:1px solid #ccc}
.news .ex{font-size:12px;line-height:21px;color:#999;margin-top:12px}
.news .btn{width:143px;height:36px;margin-top:14px;margin-left:1px}

/* footer */
.footer{left:0;top:2962px;width:1200px;height:295px;background:var(--footer)}
.fcol{top:3024px;color:var(--white);font-size:12px;line-height:21px}
.fcol h5{font-family:"Raleway",sans-serif;font-weight:500;font-size:16px;margin-bottom:18px;letter-spacing:.3px}
.flinks{display:grid;grid-template-columns:110px 110px;row-gap:14px;line-height:21px}
.frow{display:flex;gap:18px;align-items:flex-start;margin-bottom:8px}
.frow svg{flex:none;margin-top:4px}
.hours{display:grid;grid-template-columns:130px 90px;row-gap:12px;margin-top:16px}
.base{left:0;top:3257px;width:1200px;height:52px;background:var(--footer-base);color:#ddd;font-size:12px;display:flex;align-items:center}
.base .links{position:absolute;right:95px;display:flex;gap:13px}
</style>
</head>
<body>

<div class="abs topbar">
  <div class="cell social"><span></span><span></span><span></span><span></span><span></span><span></span><span></span></div>
  <div class="cell contact-mail">
    <svg width="13" height="11" viewBox="0 0 13 11"><rect x=".5" y=".5" width="12" height="10" fill="none" stroke="#999"/><path d="M.5 .5l6 5 6-5" fill="none" stroke="#999"/></svg>
    Email us: info@vorlane.co.za</div>
  <div class="cell contact-phone">
    <svg width="12" height="12" viewBox="0 0 12 12"><path d="M2 1l2 0 1 3-1.5 1a7 7 0 0 0 3.5 3.5L8 7l3 1v2a1 1 0 0 1-1 1A9 9 0 0 1 1 2a1 1 0 0 1 1-1z" fill="#999"/></svg>
    Call us: 011 555 0142</div>
</div>

<div class="abs brand">
  <div class="brand-name">VORLANE</div>
</div>

<nav class="abs nav">
  <span class="active">Home</span><span>Features</span><span>Who We Are</span><span>Our Services</span><span>Our Work</span><span>News Mega</span><span>Contact Us</span>
</nav>

<div class="abs hero" role="img" aria-label="Photo of a white hard hat, rolled plans, glasses and a keyboard on a site office desk"></div>
<div class="abs hero-shade"></div>
<h1 class="abs hero-title">Welcome To <b>VORLANE</b></h1>
<p class="abs hero-sub">Sed ut perspiciatis unde omnis iste natus error sit voluptatem accusantium doloremque laudantium</p>
<div class="abs btn btn-hero" style="left:810px;width:142px">Our Services</div>
<div class="abs btn btn-hero btn-outline" style="left:964px;width:141px">Get a Quote</div>

<h2 class="abs sec-title" style="left:506px;top:846px;width:189px;height:61px"><b>ABOUT</b><span>US</span></h2>
<div class="abs about-frame"></div>
<div class="abs about-photo" role="img" aria-label="Photo of engineers reviewing plans beside hard hats"></div>
<h3 class="abs about-h">WHO WE ARE</h3>
<p class="abs about-p">Sed ut perspiciatis unde omnis iste natus error sit voluptatem accusantium doloremque laudantium, totam rem aperiam, eaque ipsa quae ab illo inventore veritatis et quasi architecto beatae vitae dicta sunt explicabo. Nemo enim ipsam voluptatem quia voluptas sit aspernatur aut odit aut fugit, sed quia consequuntur magni dolores eos qui ratione voluptatem sequi nesciunt.</p>
<div class="abs btn" style="left:624px;top:1223px;width:143px;height:39px">Read More</div>

<div class="abs services" role="img" aria-label="Photo of a worker in a hard hat and safety vest at an industrial site"></div>
<div class="abs services-shade"></div>
<h2 class="abs sec-title light" style="left:506px;top:1466px;width:259px;height:61px"><span style="margin-left:0">OUR</span><b style="margin-left:8px">SERVICES</b></h2>

<div class="abs svc" style="left:93px">
  <svg width="80" height="74" viewBox="0 0 80 74" fill="none" stroke="#fff" stroke-width="3"><path d="M6 12h30M6 12v50h68v-40"/><path d="M6 62l10-10"/><path d="M60 4l10 10-32 32-14 4 4-14z"/><path d="M50 70l20-20v20z"/></svg>
  <h3>CONSTRUCTION</h3>
  <p>At vero eos et accusamus et iusto odio dignissimos ducimus qui blanditiis praesentium voluptatum deleniti atque corrupti quos</p>
</div>
<div class="abs svc" style="left:442px">
  <svg width="80" height="74" viewBox="0 0 80 74" fill="none" stroke="#fff" stroke-width="3"><circle cx="26" cy="50" r="18"/><path d="M38 36l8-8"/><path d="M50 24l4-4M58 16l4-4M66 8l4-4" stroke-dasharray="3 4"/><path d="M18 46a10 10 0 0 1 8-8"/></svg>
  <h3>DEMOLITION</h3>
  <p>At vero eos et accusamus et iusto odio dignissimos ducimus qui blanditiis praesentium voluptatum deleniti atque corrupti quos</p>
</div>
<div class="abs svc" style="left:790px">
  <svg width="80" height="74" viewBox="0 0 80 74" fill="none" stroke="#fff" stroke-width="3"><path d="M14 4l58 64M66 4L8 68"/><path d="M4 14c10-12 24-12 30-8M76 14c-10-12-24-12-30-8"/><path d="M20 58l8 8"/></svg>
  <h3>MINING</h3>
  <p>At vero eos et accusamus et iusto odio dignissimos ducimus qui blanditiis praesentium voluptatum deleniti atque corrupti quos</p>
</div>
<svg class="abs arrow" style="left:43px" viewBox="0 0 34 34"><circle cx="17" cy="17" r="15.5" fill="none" stroke="#fff" stroke-width="2"/><path d="M20 10l-7 7 7 7" fill="none" stroke="#fff" stroke-width="2"/></svg>
<svg class="abs arrow" style="left:1123px" viewBox="0 0 34 34"><circle cx="17" cy="17" r="15.5" fill="none" stroke="#fff" stroke-width="2"/><path d="M14 10l7 7-7 7" fill="none" stroke="#fff" stroke-width="2"/></svg>

<h2 class="abs sec-title" style="left:469px;top:2001px;width:262px;height:60px"><b style="font-weight:500">TESTIMONIALS</b></h2>
<div class="abs quote" style="left:99px">Dummy text is text that is used in the publishing industry or by web designers to occupy the space which will later be filled with ‘real’ content. This is required when, for example, the final text is not yet available.</div>
<div class="abs quote" style="left:614px">Dummy text is text that is used in the publishing industry or by web designers to occupy the space which will later be filled with ‘real’ content. This is required when, for example, the final text is not yet available.</div>
<div class="abs avatar" style="left:111px;top:2232px" role="img" aria-label="Portrait of client Daniel M. Farrow"></div>
<div class="abs person" style="left:194px;top:2270px">Daniel M. Farrow</div>
<div class="abs avatar" style="left:626px;top:2232px" role="img" aria-label="Portrait of client Marcus"></div>
<div class="abs person" style="left:709px;top:2270px">Marcus</div>

<div class="abs news-bg"></div>
<h2 class="abs sec-title" style="left:470px;top:2449px;width:261px;height:61px"><span style="margin-left:0">RECENT</span><b style="margin-left:8px">NEWS</b></h2>

<article class="abs news" style="left:94px">
  <div class="pic" role="img" aria-label="Photo of workers on steel framing at sunset" style="background:linear-gradient(180deg,#4a6fa8,#c98a4a 70%,#3a2a20)"></div>
  <h4>LOREM IPSUM DOLOR SIT AMET</h4>
  <div class="meta">December 2018, &nbsp;&nbsp; No Comments</div>
  <p class="ex">Learn how to market your contractor business professionally. In depth knowledge of attracting clients</p>
  <div class="btn">Read More</div>
</article>
<article class="abs news" style="left:443px">
  <div class="pic" role="img" aria-label="Photo of an engineer with plans at a building site" style="background:linear-gradient(180deg,#cfd8e0,#bfa88a 60%,#8a7660)"></div>
  <h4>LOREM IPSUM DOLOR SIT AMET</h4>
  <div class="meta">December 2018, &nbsp;&nbsp; No Comments</div>
  <p class="ex">Learn how to market your contractor business professionally. In depth knowledge of attracting clients</p>
  <div class="btn">Read More</div>
</article>
<article class="abs news" style="left:792px">
  <div class="pic" role="img" aria-label="Photo of an excavator loading a dump truck at a mine" style="background:linear-gradient(180deg,#9aa0a4,#5a4c40 60%,#2e2824)"></div>
  <h4>LOREM IPSUM DOLOR SIT AMET</h4>
  <div class="meta">December 2018, &nbsp;&nbsp; No Comments</div>
  <p class="ex">Learn how to market your contractor business professionally. In depth knowledge of attracting clients</p>
  <div class="btn">Read More</div>
</article>

<footer class="abs footer"></footer>
<div class="abs fcol" style="left:93px;width:225px">
  <h5>ABOUT COMPANY</h5>
  <p>Sed ut perspiciatis unde omnis iste natus error sit voluptatem accusantium dolore laudantium, totam rem aperiam, eaque ipsa quae ab illo inventore veritatis et quasi architecto beatae vitae dicta sunt explicabo.</p>
</div>
<div class="abs fcol" style="left:358px">
  <h5>COMPANY</h5>
  <div class="flinks"><span>Home</span><span>Our Work</span><span>Features</span><span>News Mega</span><span>Who We Are</span><span>Contact Us</span><span>Our Services</span></div>
</div>
<div class="abs fcol" style="left:621px;width:240px">
  <h5>CONSTRUCTION OFFICE</h5>
  <div class="frow"><svg width="10" height="13" viewBox="0 0 10 13"><path d="M5 0a5 5 0 0 1 5 5c0 3-5 8-5 8S0 8 0 5a5 5 0 0 1 5-5z" fill="#fff"/><circle cx="5" cy="5" r="2" fill="#1b1b1b"/></svg><span>42 Ridge Street<br>Kestrel Park 2194</span></div>
  <div class="frow"><svg width="10" height="11" viewBox="0 0 12 12"><path d="M2 1l2 0 1 3-1.5 1a7 7 0 0 0 3.5 3.5L8 7l3 1v2a1 1 0 0 1-1 1A9 9 0 0 1 1 2a1 1 0 0 1 1-1z" fill="#fff"/></svg><span>011 555 0142</span></div>
  <div class="frow"><svg width="11" height="9" viewBox="0 0 11 9"><rect width="11" height="9" fill="#fff"/><path d="M0 0l5.5 5L11 0" fill="none" stroke="#1b1b1b"/></svg><span>info@vorlane.co.za</span></div>
  <div class="frow"><svg width="11" height="11" viewBox="0 0 11 11"><rect x="0" y="3" width="11" height="7" fill="#fff"/><rect x="2" y="0" width="7" height="4" fill="#fff"/></svg><span>Fax: (011) 555-0143</span></div>
</div>
<div class="abs fcol" style="left:884px;width:230px">
  <h5>BUSINESS HOURS</h5>
  <p>Our support available to help you 24 hours a day, seven days a week.</p>
  <div class="hours"><span>Monday-Friday:</span><span>9am to 5pm</span><span>Saturday:</span><span>10am to 2pm</span><span>Sunday:</span><span>&nbsp;Closed</span></div>
</div>
<div class="abs base">
  <span style="margin-left:98px">Copyright © 2018. All Rights are Reserved</span>
  <div class="links"><span>Our Services</span><span>Projects</span><span>Contact Us</span><span>Disclaimer</span><span>Privacy Policy</span></div>
</div>

</body>
</html>
```